Business Card Design for Photographer

Updating business card design. Must use included logo. We're a luxury wedding photography business. Elegancy, luxury, consistency are messages we wish to convey.

Visit our website at www.colbyvarnway.com to familiarize yourself more with our brand design currently (fonts, colors etc.). This is what we want to maintain.

Target Market(s)

Luxury Brides and Grooms

Industry/Entity Type

Wedding

Contact Information for Business Card

Current logo (attached to brief)
Name: Colby Varnway
Phone: 5208813047
website/blog
Email

Requirements
Must have
• Current logo (attached to brief)
• Name: Colby Varnway
• Phone: 5208813047
• website/blog
• Email
• Instagram username
Should not have
• bright colors, fonts that don't suit our brand (visit www.colbyvarnway.com)

```html
<!DOCTYPE html>
<html lang="en">
<head>
<meta charset="utf-8">
<title>Colby Varnway Photographers – Business Card</title>
<link rel="stylesheet" href="https://fonts.googleapis.com/css2?family=Tenor+Sans&family=Open+Sans:ital,wght@0,400;0,600;1,400&family=Tinos&display=swap">
<style>
  :root {
    --backdrop: #1c1c1c;
    --card-front: #ffffff;
    --card-back: #707070;
    --ink-grey: #7a7a7a;
    --ink-soft: #9a9a9a;
    --ink-white: #ffffff;
    --lens-light: #ededed;
    --lens-mid: #d6d6d6;
    --lens-dark: #bdbdbd;
  }
  * { margin: 0; padding: 0; box-sizing: border-box; }
  html, body { width: 1200px; height: 848px; overflow: hidden; background: var(--backdrop); }
  .canvas { position: relative; width: 1200px; height: 848px; }

  .card { position: absolute; overflow: hidden; }
  .card-front { left: 255px; top: 57px; width: 644px; height: 368px; background: var(--card-front); }
  .card-back { left: 256px; top: 446px; width: 642px; height: 364px; background: var(--card-back); }

  .lens-photo { position: absolute; left: 0; top: 0; }

  .brand { position: absolute; left: 339px; top: 27px; width: 240px; text-align: center; color: var(--ink-grey); font-family: "Tenor Sans", sans-serif; }
  .brand-square { display: block; width: 44px; height: 44px; margin: 0 auto 18px; background: var(--ink-grey); }
  .brand-name { font-size: 21px; letter-spacing: 4px; line-height: 1; white-space: nowrap; }
  .brand-sub { font-size: 11px; letter-spacing: 4.6px; margin-top: 10px; white-space: nowrap; }

  .contact { position: absolute; left: 338px; top: 225px; font-family: "Open Sans", sans-serif; color: var(--ink-grey); }
  .contact-name { font-size: 25px; margin-left: 25px; line-height: 1; margin-bottom: 8px; }
  .contact-line { display: flex; align-items: center; font-size: 15px; line-height: 22px; color: var(--ink-soft); }
  .contact-line em { font-style: italic; }
  .contact-line svg { width: 16px; height: 16px; margin-right: 9px; flex: none; }
  .contact-phone { font-size: 24px; font-weight: 600; color: var(--ink-grey); line-height: 30px; margin-top: 1px; }
  .contact-phone svg { width: 16px; height: 16px; margin-right: 3px; }

  .back-phone { position: absolute; left: 0; right: 0; top: 166px; text-align: center; font-family: "Tinos", serif; font-size: 54px; color: var(--ink-white); line-height: 1; }
  .back-links { position: absolute; top: 326px; font-family: "Open Sans", sans-serif; font-size: 13px; color: var(--ink-white); }
  .back-links span { position: absolute; white-space: nowrap; }
</style>
</head>
<body>
<div class="canvas">

  <section class="card card-front">
    <svg class="lens-photo" width="300" height="368" viewBox="0 0 300 368" role="img" aria-label="Close-up photograph of a camera lens, soft grey tones">
      <defs>
        <radialGradient id="lensTone" cx="0.15" cy="0.35" r="0.9">
          <stop offset="0" stop-color="var(--lens-dark)"/>
          <stop offset="0.55" stop-color="var(--lens-mid)"/>
          <stop offset="1" stop-color="var(--lens-light)"/>
        </radialGradient>
      </defs>
      <circle cx="-6" cy="142" r="300" fill="url(#lensTone)"/>
    </svg>

    <div class="brand">
      <span class="brand-square"></span>
      <div class="brand-name">COLBY VARNWAY</div>
      <div class="brand-sub">PHOTOGRAPHERS</div>
    </div>

    <div class="contact">
      <div class="contact-name">Colby Varnway</div>
      <div class="contact-line">
        <svg viewBox="0 0 16 16"><rect x="1" y="3" width="14" height="10" fill="var(--ink-grey)"/><path d="M1 3 L8 9 L15 3" fill="none" stroke="#fff" stroke-width="1"/></svg>
        colby@colbyvarnway.com
      </div>
      <div class="contact-line">
        <svg viewBox="0 0 16 16"><circle cx="8" cy="8" r="6.5" fill="none" stroke="var(--ink-grey)" stroke-width="1.5"/><ellipse cx="8" cy="8" rx="2.8" ry="6.5" fill="none" stroke="var(--ink-grey)" stroke-width="1.2"/><line x1="1.5" y1="8" x2="14.5" y2="8" stroke="var(--ink-grey)" stroke-width="1.2"/></svg>
        <em>www.colbyvarnway.com</em>
      </div>
      <div class="contact-line">
        <svg viewBox="0 0 16 16"><rect x="2" y="2" width="12" height="12" fill="var(--ink-grey)"/></svg>
        <em>colbyvarnwayphoto</em>
      </div>
      <div class="contact-line contact-phone">
        <svg viewBox="0 0 16 16"><circle cx="8" cy="8" r="7" fill="none" stroke="var(--ink-grey)" stroke-width="1.5"/><path d="M5.5 4.5 L7 4.5 L7.5 6.5 L6.6 7.2 Q7.5 9 8.8 9.4 L9.5 8.5 L11.5 9 L11.5 10.5 Q8 11.5 5.5 7.5 Z" fill="var(--ink-grey)"/></svg>
        520. 881. 3047
      </div>
    </div>
  </section>

  <section class="card card-back">
    <div class="back-phone">520. 881. 3047</div>
    <div class="back-links">
      <span style="left:47px">www.colbyvarnway.com</span>
      <span style="left:237px">colby@colbyvarnway.com</span>
      <span style="left:413px">www.colbyvarnway.com/blog</span>
    </div>
  </section>

</div>
</body>
</html>
```